Business card for plumber

I need a business card for my plumbing company.
on it should:
Surname
position
E-mail
Telephone & mobile phone
Website
Please everything as placeholders / fantasy names.
We stand for high quality, hygiene and professionalism.

Colours:
# 606060 anthracite
# f7931e orange
# 2b89cc blue

Industry/Entity Type

Plumber

Contact Information for Business Card

folgt...

```html
<!DOCTYPE html>
<html lang="en">
<head>
<meta charset="utf-8">
<title>Feldmark Haustechnik – Business Card</title>
<link rel="stylesheet" href="https://fonts.googleapis.com/css2?family=Arimo:wght@400;700&display=swap">
<style>
  :root {
    --anthracite: #606060;
    --orange: #f7931e;
    --blue: #2b89cc;
    --card: #ffffff;
    --backdrop: #2a2a2c;
  }
  * { box-sizing: border-box; margin: 0; padding: 0; }
  html, body {
    width: 1200px;
    height: 1189px;
    overflow: hidden;
    background: var(--backdrop);
    font-family: "Arimo", Arial, sans-serif;
  }
  .sheet {
    position: relative;
    width: 1200px;
    height: 1189px;
  }
  .card {
    position: absolute;
    left: 150px;
    width: 900px;
    height: 514px;
    background: var(--card);
    border-radius: 36px;
    box-shadow: 0 10px 30px rgba(0,0,0,.45);
  }
  .card--back { top: 50px; }
  .card--front { top: 614px; }

  /* company name set as plain text */
  .wordmark {
    display: flex;
    align-items: center;
    gap: 22px;
    color: var(--blue);
    font-weight: 700;
    text-transform: uppercase;
  }
  .wordmark__dot {
    flex: none;
    border-radius: 50%;
    background: var(--orange);
  }
  .wordmark__text { line-height: .95; }
  .wordmark__sub { display: block; letter-spacing: .42em; }

  .card--back .wordmark {
    position: absolute;
    left: 170px;
    top: 160px;
  }
  .card--back .wordmark__dot { width: 110px; height: 110px; }
  .card--back .wordmark__text { font-size: 64px; }
  .card--back .wordmark__sub { font-size: 32px; margin-top: 6px; }

  .services {
    position: absolute;
    left: 0;
    right: 0;
    bottom: 110px;
    text-align: center;
    color: var(--anthracite);
    font-size: 24px;
    letter-spacing: .04em;
    text-transform: uppercase;
  }
  .services__sep { color: var(--orange); margin: 0 8px; }

  .card--front .wordmark {
    position: absolute;
    left: 70px;
    top: 70px;
  }
  .card--front .wordmark__dot { width: 22px; height: 22px; }
  .card--front .wordmark__text { font-size: 62px; }
  .card--front .wordmark__sub { font-size: 30px; margin-top: 6px; }

  .person {
    position: absolute;
    left: 70px;
    top: 245px;
  }
  .person__name {
    color: var(--blue);
    font-weight: 700;
    font-size: 32px;
    letter-spacing: .02em;
  }
  .person__role {
    color: var(--orange);
    font-size: 24px;
    margin-top: 2px;
  }
  .contact {
    list-style: none;
    margin-top: 26px;
  }
  .contact__item {
    display: flex;
    align-items: center;
    gap: 16px;
    height: 34px;
    color: var(--anthracite);
    font-size: 24px;
  }
  .contact__icon {
    width: 26px;
    height: 26px;
    flex: none;
  }
  .contact__accent { color: var(--orange); }
</style>
</head>
<body>
<main class="sheet">

  <section class="card card--back" aria-label="Card back">
    <div class="wordmark">
      <span class="wordmark__dot"></span>
      <span class="wordmark__text">Feldmark<span class="wordmark__sub">Haustechnik</span></span>
    </div>
    <p class="services">
      <span class="services__sep">•</span>Plumbing<span class="services__sep">•</span>Heating 24h Emergency<span class="services__sep">•</span>Maintenance
    </p>
  </section>

  <section class="card card--front" aria-label="Card front">
    <div class="wordmark">
      <span class="wordmark__text">Feldmark<span class="wordmark__sub">Haustechnik</span></span>
    </div>

    <div class="person">
      <h1 class="person__name">LUKAS BERGER</h1>
      <p class="person__role">Manager</p>
      <ul class="contact">
        <li class="contact__item">
          <svg class="contact__icon" viewBox="0 0 26 26" aria-hidden="true">
            <circle cx="13" cy="13" r="13" fill="#f7931e"/>
            <rect x="9" y="6" width="8" height="14" rx="1.5" fill="none" stroke="#fff" stroke-width="1.6"/>
            <line x1="12" y1="17.5" x2="14" y2="17.5" stroke="#fff" stroke-width="1.4"/>
          </svg>
          +1 555 014 2290
        </li>
        <li class="contact__item">
          <svg class="contact__icon" viewBox="0 0 26 26" aria-hidden="true">
            <circle cx="13" cy="13" r="13" fill="#f7931e"/>
            <path d="M6 11c0-3 14-3 14 0v1.5h-3.5v-2h-7v2H6z" fill="#fff"/>
            <rect x="8" y="13" width="10" height="6" rx="1.2" fill="#fff"/>
          </svg>
          +1 555 014 2291
        </li>
        <li class="contact__item">
          <svg class="contact__icon" viewBox="0 0 26 26" aria-hidden="true">
            <circle cx="13" cy="13" r="13" fill="#f7931e"/>
            <rect x="6.5" y="8.5" width="13" height="9" fill="none" stroke="#fff" stroke-width="1.5"/>
            <polyline points="6.5,8.5 13,14 19.5,8.5" fill="none" stroke="#fff" stroke-width="1.5"/>
          </svg>
          info@feldmark-mail.com
        </li>
        <li class="contact__item">
          <svg class="contact__icon" viewBox="0 0 26 26" aria-hidden="true">
            <circle cx="13" cy="13" r="13" fill="#f7931e"/>
            <circle cx="13" cy="13" r="6.5" fill="none" stroke="#fff" stroke-width="1.4"/>
            <ellipse cx="13" cy="13" rx="2.8" ry="6.5" fill="none" stroke="#fff" stroke-width="1.2"/>
            <line x1="6.5" y1="13" x2="19.5" y2="13" stroke="#fff" stroke-width="1.2"/>
          </svg>
          www.<span class="contact__accent">feldmark-haus</span>.com
        </li>
      </ul>
    </div>
  </section>

</main>
</body>
</html>
```